Card Design to Advertise New Business

I am looking to have a card designed so that I can pass it out to help promote my business. I have never done this before so I honestly do not know where to start with any ideas. I am providing my website address to help. I provide math tutoring, test prep, and schooling options.

I am looking for a card bigger than a business card but smaller than a flyer. Something front and back that I can pass out.

Business Information
Phone: 470-555-0192
Website: www.kelvanostudyhall.example
Address: 418 Brackenfield Rd Ste 340 Marietta GA 30072
Email: kelvanoservices@kelvanomail.example

Services:
Math Tutoring
NEQ & BOW Test Prep
Group and Private Sessions
Fully Accredited Private School

Target Market(s)

Middle and High School Students

Industry/Entity Type

Education

Requirements
Must have
• Information from my website

```html
<!DOCTYPE html>
<html lang="en">
<head>
<meta charset="utf-8">
<title>Kelvano Study Hall – Promo Card</title>
<link rel="stylesheet" href="https://fonts.googleapis.com/css2?family=Oswald:wght@500;600&family=Open+Sans:wdth,wght@75..100,400..700&display=swap">
<style>
  :root {
    --purple: #4f4a9a;
    --rust: #bb4423;
    --rust-dark: #b13d1c;
    --blue: #3b4fb8;
    --ink-muted: #5a5690;
    --paper: #ffffff;
    --stage: #e9e9ec;
  }
  * { margin: 0; padding: 0; box-sizing: border-box; }
  html, body { width: 1200px; height: 1002px; overflow: hidden; }
  body {
    background: var(--stage);
    font-family: "Open Sans", sans-serif;
    position: relative;
  }
  .card {
    position: absolute;
    left: 255px;
    width: 690px;
    height: 460px;
    background: var(--paper);
    overflow: hidden;
    box-shadow: 0 2px 10px rgba(0,0,0,.12);
  }
  .card--front { top: 27px; }
  .card--back { top: 515px; }

  /* ---------- Front ---------- */
  .brand {
    position: absolute;
    display: flex;
    align-items: center;
    gap: 12px;
  }
  .brand__mark {
    border-radius: 50%;
    background: var(--blue);
    flex: none;
  }
  .brand__name {
    font-family: "Oswald", sans-serif;
    font-weight: 600;
    color: var(--blue);
    line-height: 1;
    text-transform: uppercase;
  }
  .card--front .brand { left: 24px; top: 22px; }
  .card--front .brand__mark { width: 110px; height: 110px; }
  .card--front .brand__name { font-size: 30px; width: 200px; }

  .front__photo {
    position: absolute;
    right: 0; top: 28px;
    width: 330px; height: 362px;
    background: radial-gradient(ellipse at 72% 45%, #e3b99c 0%, #c99b7e 22%, #7d5a44 40%, #dfe4ec 62%, rgba(255,255,255,0) 80%);
  }
  .services {
    position: absolute;
    left: 38px; top: 168px;
    list-style: none;
  }
  .services li {
    position: relative;
    padding-left: 44px;
    font-family: "Oswald", sans-serif;
    font-weight: 500;
    font-size: 25px;
    line-height: 30px;
    color: var(--rust);
    margin-bottom: 7px;
    width: 270px;
  }
  .services li::before {
    content: "";
    position: absolute;
    left: 0; top: 6px;
    width: 24px; height: 24px;
    border-radius: 50%;
    background: var(--purple);
  }
  .info-band {
    position: absolute;
    left: 0; bottom: 0;
    width: 100%; height: 70px;
    background: var(--rust);
    display: flex;
    align-items: center;
  }
  .info-band__label {
    position: absolute;
    left: 0; top: 0;
    width: 202px; height: 70px;
    background: var(--purple);
    clip-path: polygon(0 0, 172px 0, 202px 35px, 172px 70px, 0 70px);
    color: var(--rust);
    font-stretch: 75%;
    font-weight: 600;
    font-size: 16px;
    line-height: 19px;
    padding: 16px 0 0 82px;
  }
  .info-band__details {
    position: absolute;
    left: 215px; top: 15px;
    color: #fff;
    font-stretch: 75%;
    font-weight: 700;
    font-size: 15px;
    line-height: 21px;
    white-space: nowrap;
  }

  /* ---------- Back ---------- */
  .card--back .brand { left: 24px; top: 20px; flex-direction: column; align-items: flex-start; gap: 8px; }
  .card--back .brand__mark { width: 76px; height: 76px; margin-left: 30px; }
  .card--back .brand__name { font-size: 18px; }

  .mission {
    position: absolute;
    left: 298px; top: 46px;
    width: 110px;
  }
  .mission h3, .panel h3 {
    font-size: 10.5px;
    font-weight: 700;
    margin-bottom: 5px;
  }
  .mission h3 { color: var(--rust); }
  .mission p {
    color: var(--ink-muted);
    font-size: 8px;
    line-height: 11.5px;
  }
  .back__photo {
    position: absolute;
    left: 0; top: 150px;
    width: 428px; height: 288px;
    background: linear-gradient(180deg, #f4f4f4 0%, #eeeeee 55%, #c79a6b 80%, #a87447 100%);
  }
  .panel {
    position: absolute;
    left: 428px; top: 0;
    width: 262px; height: 438px;
    background: var(--purple);
    color: #fff;
    padding: 46px 24px 0 24px;
  }
  .panel p {
    font-size: 8px;
    line-height: 11.6px;
  }
  .panel h3 + p { margin-bottom: 24px; }
  .panel h3.panel__service { line-height: 14px; }
  .back__band {
    position: absolute;
    left: 0; bottom: 0;
    width: 100%; height: 22px;
    background: var(--rust-dark);
  }
</style>
</head>
<body>

<section class="card card--front">
  <div class="brand">
    <span class="brand__mark"></span>
    <span class="brand__name">Kelvano Study Hall</span>
  </div>

  <div class="front__photo" role="img" aria-label="Photo of a smiling schoolboy reaching toward floating colourful numbers"></div>

  <ul class="services">
    <li>Math Tutoring</li>
    <li>NEQ &amp; BOW Test Prep</li>
    <li>Group and Private Sessions</li>
    <li>Fully Accredited Private School</li>
  </ul>

  <div class="info-band">
    <div class="info-band__label">Business Information</div>
    <div class="info-band__details">
      418 Brackenfield Rd Ste 340 Marietta GA 30072 &nbsp;|&nbsp; T: 470-555-0192<br>
      E: kelvanoservices@kelvanomail.example &nbsp;|&nbsp; W: www.kelvanostudyhall.example
    </div>
  </div>
</section>

<section class="card card--back">
  <div class="brand">
    <span class="brand__mark"></span>
    <span class="brand__name">Kelvano Study Hall</span>
  </div>

  <div class="mission">
    <h3>Our Mission:</h3>
    <p>To use optimistic mindsets to teach others to be confident in taking risks despite life’s current and possible challenges.</p>
  </div>

  <div class="back__photo" role="img" aria-label="Photo of a young girl writing at a desk with books, an apple, coloured pencils and equations on the wall"></div>

  <aside class="panel">
    <h3>Our Vision:</h3>
    <p>Through being positive role models, presenting the best version of ourselves, focused and optimistic, we will teach, with vulnerability and confidence, the need to discover the meaning of life’s progression from one experience to the next. We will teach that everything has a purpose and is continuously adapting. Being the example to those who feel bounded, that life’s challenges is simply the preparation to becoming the best version of you.</p>
    <h3 class="panel__service">Study Coaching and Math Tutoring for all ages</h3>
    <p>Our goal is to not only build math competency but build self-confidence to perform better in classes and tests and any other paths you choose to take in life. We will work to heighten creativity, improve concentration, lower stress, and increase self-awareness. We are not “homework” tutors. Even though during our sessions we may choose to go over your homework, we are working to identify and target why you are having challenges and correct those issues. As you grow, we will continue to motivate and challenge you to become better and better. We are here to help empower everyone to help take charge of their path in life to make all their dreams a reality no matter the challenges that are in front of them. We will assist in enabling you to reach your full potential to achieve your life goals to make your dreams a reality!</p>
  </aside>

  <div class="back__band"></div>
</section>

</body>
</html>
```